Front Yard Sign for Real Estate Company

Bright Porch Keys is a brand new real estate broker. We need signs to put in front yard of houses that we are selling. 3D would be great. I have included the company LOGO

Target Market(s)

Residential Property buyers and sellers

Industry/Entity Type

Real Estate

Colors
ec1f27
ffc214
fbed22
ffffff

Requirements
Must have
• 3D look would be great. Logo must be included in the yard signs.
• Must include phone # to call: 614-290-4417

```html
<!DOCTYPE html>
<html lang="en">
<head>
<meta charset="utf-8">
<title>Bright Porch Keys – Yard Sign</title>
<link href="https://fonts.googleapis.com/css2?family=Anton&family=Montserrat:ital,wght@0,600;0,700;1,500&family=Open+Sans:wght@800&display=swap" rel="stylesheet">
<style>
  :root{
    --brand-red:#ec1f27;
    --brand-red-deep:#c8141c;
    --brand-gold:#ffc214;
    --brand-white:#ffffff;
    --ink-grey:#555556;
    --line-grey:#9a9a9a;
    --backdrop:#ececec;
  }
  html,body{margin:0;padding:0;width:698px;height:1200px;overflow:hidden;background:var(--backdrop);}
  .canvas{position:relative;width:698px;height:1200px;}
  .yard-sign{
    position:absolute;left:19px;top:380px;width:660px;height:440px;
    background:var(--brand-white);overflow:hidden;
    box-shadow:0 10px 24px rgba(0,0,0,.22);
  }
  .sign-swoosh{position:absolute;inset:0;width:100%;height:100%;}
  .brand-lockup{
    position:absolute;left:0;width:570px;top:100px;
    display:flex;align-items:center;justify-content:center;gap:10px;
  }
  .brand-dot{width:26px;height:26px;border-radius:50%;background:var(--brand-gold);}
  .brand-name{
    font-family:"Montserrat",sans-serif;font-weight:700;font-size:36px;
    color:var(--brand-red);letter-spacing:-.5px;line-height:1;
  }
  .brand-tagline{
    position:absolute;left:0;width:570px;top:152px;
    display:flex;align-items:center;justify-content:center;gap:8px;
    font-family:"Montserrat",sans-serif;font-style:italic;font-weight:500;
    font-size:12.5px;color:var(--brand-red);
  }
  .brand-tagline::before,.brand-tagline::after{
    content:"";width:36px;height:1.5px;background:var(--brand-gold);
  }
  .sale-headline{
    position:absolute;left:0;width:570px;top:184px;margin:0;text-align:center;
    font-family:"Anton",sans-serif;font-weight:400;font-size:118px;line-height:1.05;
    color:var(--brand-red);letter-spacing:1px;
    text-shadow:2px 2px 0 #7a0d12, 3px 3px 0 #222;
  }
  .sale-phone{
    position:absolute;left:0;width:570px;top:312px;text-align:center;
    font-family:"Open Sans",sans-serif;font-weight:800;font-size:54px;
    line-height:1;color:var(--ink-grey);letter-spacing:-.5px;
  }
  .sale-web{
    position:absolute;left:155px;top:388px;width:260px;height:27px;
    border:1.5px solid var(--line-grey);box-sizing:border-box;
    display:flex;align-items:center;justify-content:center;
    font-family:"Montserrat",sans-serif;font-weight:600;font-size:16px;color:var(--ink-grey);
  }
  .sale-web b{color:var(--brand-red);font-weight:700;}
</style>
</head>
<body>
<main class="canvas">
  <section class="yard-sign">
    <svg class="sign-swoosh" viewBox="0 0 660 440" preserveAspectRatio="none" aria-hidden="true">
      <defs>
        <linearGradient id="redPanel" x1="0" y1="0" x2="0" y2="1">
          <stop offset="0" stop-color="#ec1f27"/>
          <stop offset="1" stop-color="#c8141c"/>
        </linearGradient>
      </defs>
      <path d="M350 0 H382 C540 80 620 260 630 440 H596 C585 270 510 95 350 0 Z" fill="#ffc214"/>
      <path d="M388 0 H660 V440 H636 C626 258 548 80 388 0 Z" fill="url(#redPanel)"/>
    </svg>
    <div class="brand-lockup">
      <span class="brand-dot"></span>
      <span class="brand-name">Bright Porch Keys</span>
    </div>
    <div class="brand-tagline">Your key to a brighter home</div>
    <h1 class="sale-headline">FOR SALE</h1>
    <div class="sale-phone">614-290-4417</div>
    <div class="sale-web">www.<b>brightporchkeys</b>.com</div>
  </section>
</main>
</body>
</html>
```